Dale Harwick Realtors
Stationary, Letterhead, Business Cards & Envelopes
Modern
Dale Harwick
Broker/ Owner
5817 Elmwood Crest Rd.
Fort Worth, Texas 76243
daleharwick@vesnamail.net
www.DaleHarwickRealtors.com
I would like the back to be the logo and I am not sure if it should have a white background or some color, I am open.
use logo here

```html
<!DOCTYPE html>
<html lang="en">
<head>
<meta charset="utf-8">
<title>Dale Harwick Realtors – Business Cards</title>
<link rel="stylesheet" href="https://fonts.googleapis.com/css2?family=Cinzel:wght@400;600&family=Open+Sans:wght@400;600&display=swap">
<style>
  :root {
    --page: #e8e5e1;
    --navy: #1e2d6e;
    --navy-deep: #0b1240;
    --navy-mid: #1b2a78;
    --accent-blue: #3a63b8;
    --ink: #3a3a3a;
    --charcoal: #2e2e33;
    --charcoal-deep: #0c0c0f;
    --white: #ffffff;
    --swoosh: #c9ccd4;
  }
  * { margin: 0; padding: 0; box-sizing: border-box; }
  html, body { width: 1200px; height: 742px; overflow: hidden; }
  body { background: var(--page); position: relative; font-family: "Open Sans", sans-serif; }

  .card {
    position: absolute; width: 572px; height: 306px; border-radius: 20px;
    overflow: hidden; box-shadow: 0 4px 14px rgba(0,0,0,.25);
  }
  .card--front { left: 14px; top: 55px; background: var(--white); }
  .card--back-blue { left: 605px; top: 55px; background: radial-gradient(ellipse at 50% 45%, var(--navy-mid), var(--navy-deep) 80%); }
  .card--back-dark { left: 14px; top: 384px; background: radial-gradient(ellipse at 50% 40%, var(--charcoal), var(--charcoal-deep) 85%); }
  .card--back-large { left: 605px; top: 384px; background: radial-gradient(ellipse at 50% 40%, var(--navy-mid), var(--navy-deep) 85%); }

  .mark-square { display: block; background: var(--accent-blue); }

  /* Front */
  .front-brand { position: absolute; left: 22px; top: 20px; width: 300px; text-align: center; }
  .front-brand .mark-square { width: 46px; height: 46px; margin: 0 auto 6px; }
  .front-brand__name { font-family: "Cinzel", serif; font-size: 38px; color: var(--navy); line-height: 1; }
  .front-brand__tag { font-family: "Cinzel", serif; font-size: 14px; letter-spacing: 7px; color: var(--navy); margin-top: 4px; }

  .front-address { position: absolute; left: 22px; top: 170px; font-size: 12px; line-height: 1.45; color: var(--ink); }

  .front-contact { position: absolute; left: 330px; top: 138px; list-style: none; font-size: 12px; color: var(--ink); }
  .front-contact li { display: flex; align-items: center; height: 17px; }
  .front-contact svg { width: 11px; height: 11px; margin-right: 8px; fill: var(--navy); }
  .front-contact .web { color: var(--navy); }

  .front-wave { position: absolute; left: 0; bottom: 0; width: 572px; height: 306px; }
  .front-person { position: absolute; left: 22px; bottom: 18px; color: var(--white); }
  .front-person__name { font-family: "Cinzel", serif; font-size: 22px; font-weight: 600; line-height: 1.1; }
  .front-person__title { font-size: 13px; }

  /* Backs */
  .back-brand { position: absolute; inset: 0; display: flex; flex-direction: column; align-items: center; justify-content: center; color: var(--white); }
  .back-brand .mark-square { width: 46px; height: 46px; margin-bottom: 12px; }
  .back-brand__name { font-family: "Cinzel", serif; font-size: 40px; line-height: 1; }
  .back-brand__tag { font-family: "Cinzel", serif; font-size: 15px; letter-spacing: 8px; margin-top: 6px; }

  .back-large { position: absolute; inset: 0 0 60px; display: flex; flex-direction: column; align-items: center; justify-content: center; color: var(--white); }
  .back-large .mark-square { width: 96px; height: 96px; margin-bottom: 12px; }
  .back-large__name { font-family: "Cinzel", serif; font-size: 26px; }
  .back-web { position: absolute; left: 0; right: 0; bottom: 38px; text-align: center; color: var(--white); font-size: 13px; letter-spacing: 3px; }
</style>
</head>
<body>

<section class="card card--front">
  <svg class="front-wave" viewBox="0 0 572 306" aria-hidden="true">
    <defs>
      <linearGradient id="waveBlue" x1="0" y1="0" x2="1" y2="0">
        <stop offset="0" stop-color="#1e2d6e"/>
        <stop offset="1" stop-color="#2c4aa0"/>
      </linearGradient>
    </defs>
    <path d="M0 222 C150 200 300 196 400 206 C480 214 540 192 572 168" fill="none" stroke="var(--swoosh)" stroke-width="6"/>
    <path d="M0 232 C150 212 300 206 400 216 C480 224 540 204 572 182 L572 306 L0 306 Z" fill="url(#waveBlue)"/>
  </svg>

  <div class="front-brand">
    <span class="mark-square"></span>
    <div class="front-brand__name">Dale Harwick</div>
    <div class="front-brand__tag">REALTORS</div>
  </div>

  <address class="front-address" style="font-style:normal">
    5817 Elmwood Crest Rd.<br>Fort Worth, Texas 76243
  </address>

  <ul class="front-contact">
    <li><svg viewBox="0 0 12 12"><path d="M2 1h2l1 3-1.5 1a7 7 0 0 0 3.5 3.5L8 7l3 1v2a1 1 0 0 1-1 1A9 9 0 0 1 1 2a1 1 0 0 1 1-1z"/></svg>817-555-0142</li>
    <li><svg viewBox="0 0 12 12"><rect x="3" y="0.5" width="6" height="11" rx="1"/></svg>817-555-0187</li>
    <li><svg viewBox="0 0 12 12"><path d="M0 2h12v8H0z M0 2l6 4 6-4" /></svg>daleharwick@vesnamail.net</li>
    <li class="web"><svg viewBox="0 0 12 12"><circle cx="6" cy="6" r="5.5"/></svg>www.DaleHarwickRealtors.com</li>
  </ul>

  <div class="front-person">
    <div class="front-person__name">Dale Harwick</div>
    <div class="front-person__title">Broker / Owner</div>
  </div>
</section>

<section class="card card--back-blue">
  <div class="back-brand">
    <span class="mark-square"></span>
    <div class="back-brand__name">DaleHarwick</div>
    <div class="back-brand__tag">REALTORS</div>
  </div>
</section>

<section class="card card--back-dark">
  <div class="back-large">
    <span class="mark-square"></span>
    <div class="back-large__name">Dale Harwick</div>
  </div>
  <div class="back-web">www.DaleHarwickRealtors.com</div>
</section>

<section class="card card--back-large">
  <div class="back-large">
    <span class="mark-square"></span>
    <div class="back-large__name">Dale Harwick</div>
  </div>
  <div class="back-web">www.DaleHarwickRealtors.com</div>
</section>

</body>
</html>
```